Vorna Fleet business card

I am needing a business card that at a glance shows all the services that we provide emphasizing some more than others. We are a Fleet and Compliance management company as well as a software company. We provide outsourced solutions for KPX compliance and HR services via our own software.
In addition, we do
drug testing
GPS
Cameras
Electronic DVIRS
ELD's

Target Market(s)

Transportation company owners

Industry/Entity Type

Transportation supplier

Contact Information for Business Card

the card should inform potential customers what we do

Other font styles liked:
• I have added brand guidelines. See attached

Requirements
Must have
• See description
Should not have
• Colors outside my brand guide. See attached

```html
<!DOCTYPE html>
<html lang="en">
<head>
<meta charset="UTF-8">
<title>Vorna Fleet business card</title>
<link rel="stylesheet" href="https://fonts.googleapis.com/css2?family=Open+Sans:wght@400;600;700&display=swap">
<style>
  :root {
    --brand-red: #ee2a32;
    --brand-black: #0a0a0c;
    --brand-grey: #b5b5b7;
    --text-grey: #5a5a5c;
    --paper: #ffffff;
    --page: #ffffff;
  }
  html, body {
    margin: 0;
    padding: 0;
    width: 1200px;
    height: 1142px;
    overflow: hidden;
    background: var(--page);
    font-family: "Open Sans", Arial, sans-serif;
  }
  .card {
    position: absolute;
    left: 357px;
    top: 374px;
    width: 498px;
    height: 321px;
    background: var(--paper);
    box-shadow: 4px 5px 8px rgba(0,0,0,0.25);
    overflow: hidden;
  }
  .card-art {
    position: absolute;
    inset: 0;
    width: 498px;
    height: 321px;
  }
  .brand-name {
    position: absolute;
    left: 34px;
    top: 62px;
    margin: 0;
    font-size: 22px;
    font-weight: 700;
    line-height: 30px;
    color: var(--brand-black);
    white-space: nowrap;
  }
  .services {
    position: absolute;
    left: 34px;
    top: 104px;
    margin: 0;
    padding: 0;
    list-style: none;
    white-space: nowrap;
  }
  .service-lead {
    font-size: 10.5px;
    font-weight: 700;
    line-height: 15px;
    color: var(--brand-red);
  }
  .service-main {
    font-size: 9.5px;
    font-weight: 600;
    line-height: 14px;
    color: var(--brand-black);
  }
  .service-extra {
    font-size: 9px;
    font-weight: 400;
    line-height: 13px;
    color: var(--text-grey);
  }
  .person {
    position: absolute;
    right: 24px;
    top: 70px;
    text-align: right;
  }
  .person-name {
    margin: 0;
    font-size: 17px;
    font-weight: 600;
    line-height: 22px;
    color: var(--brand-red);
    letter-spacing: 0.3px;
  }
  .person-title {
    margin: 0;
    font-size: 11px;
    line-height: 16px;
    color: #d4d4d6;
    letter-spacing: 2.4px;
  }
  .contact-list {
    position: absolute;
    right: 49px;
    top: 211px;
    margin: 0;
    padding: 0;
    list-style: none;
    text-align: right;
    font-size: 14.5px;
    line-height: 22.5px;
    color: var(--text-grey);
  }
  .phone-list {
    position: absolute;
    left: 50px;
    top: 233px;
    margin: 0;
    padding: 0;
    list-style: none;
    font-size: 13.5px;
    line-height: 19.5px;
    color: var(--text-grey);
    letter-spacing: 0.6px;
  }
</style>
</head>
<body>
  <section class="card" aria-label="Vorna Fleet business card">
    <svg class="card-art" viewBox="0 0 332 214" aria-hidden="true">
      <polygon fill="var(--brand-red)" points="0,0 110,0 119,20 0,20"/>
      <polygon fill="var(--brand-black)" points="138,0 332,0 332,92 182,92"/>
      <polygon fill="var(--brand-grey)" points="110,0 138,0 182,92 174,134 164,134"/>
      <polygon fill="var(--brand-red)" points="182,92 196,92 184,134 174,134"/>
      <polygon fill="var(--brand-grey)" points="0,188 137,188 150,214 0,214"/>
      <polygon fill="var(--brand-red)" points="137,188 332,188 332,214 150,214"/>
      <g fill="var(--brand-red)">
        <rect x="311" y="145.5" width="8" height="5.5" rx="0.6"/>
        <path d="M311.3 146 L315 149 L318.7 146" fill="none" stroke="#fff" stroke-width="0.7"/>
        <path d="M315 158 a3.2 3.2 0 0 1 3.2 3.2 c0 2.2 -3.2 5.3 -3.2 5.3 s-3.2 -3.1 -3.2 -5.3 A3.2 3.2 0 0 1 315 158 z"/>
        <circle cx="315" cy="161.2" r="1.2" fill="#fff"/>
        <circle cx="315" cy="178" r="3.6"/>
        <g fill="none" stroke="#fff" stroke-width="0.5">
          <ellipse cx="315" cy="178" rx="1.5" ry="3.6"/>
          <line x1="311.4" y1="178" x2="318.6" y2="178"/>
        </g>
        <path d="M18 158.6 c0.8 -0.8 1.6 -0.6 2.2 0.2 l0.8 1.2 c0.3 0.5 0.2 1 -0.3 1.4 l-0.6 0.5 c0.6 1.2 1.4 2 2.6 2.6 l0.5 -0.6 c0.4 -0.5 0.9 -0.6 1.4 -0.3 l1.2 0.8 c0.8 0.6 1 1.4 0.2 2.2 c-1 1 -2.6 0.9 -4.2 -0.1 c-1.6 -1 -3 -2.4 -4 -4 c-1 -1.6 -1.1 -3.2 -0.2 -4.2 z"/>
        <rect x="19" y="170.5" width="4.6" height="8" rx="0.8"/>
        <rect x="19.9" y="171.6" width="2.8" height="5" fill="#fff"/>
      </g>
    </svg>

    <p class="brand-name">Vorna Fleet</p>

    <ul class="services" aria-label="Services">
      <li class="service-lead">KPX Compliance · HR Software</li>
      <li class="service-main">Fleet Management Solutions</li>
      <li class="service-extra">Drug Testing · GPS · Cameras</li>
      <li class="service-extra">Electronic DVIRs · ELDs</li>
    </ul>

    <div class="person">
      <p class="person-name">PERSONS NAME</p>
      <p class="person-title">PERSONS TITLE</p>
    </div>

    <ul class="contact-list">
      <li>aaaaaaa@nnn.com</li>
      <li>City, State Name, 77</li>
      <li>www.sssssssss.com</li>
    </ul>

    <ul class="phone-list">
      <li>(999) 222-5555</li>
      <li>(999) 222-4444</li>
    </ul>
  </section>
</body>
</html>
```